Editable Flyer Layout for MIDWAY PARCELRUN

to come up with a flyer layout that has editable spots to change promotions from time to time. We are a courier company in Calgary Alberta. Our logos and color schemes can be viewed on our website www.haulbrisk.example We are wanting something that fits with website but more of an edge on the print media side. Our website also feature our "Focus" page which will tell you about us and our practices. Please conside this when constructing flyer. We also have additional image files for you if needed.

Thanks !!!!
Updates

Some of these designs are great. Never expected to get so many different results. I will comment on potential designs once we have reviewed all and only after deadline. For now Thanks to all .....!!!!!

Thank you all for your submissions. Some have been eliminated. Those that have not I have sent message to you. The designs look great but need some minor changes. I have sent some suggestions and revert back to you. Please review the notes above on ad (promo) and the editable space.

Thanks Very Much !!!

Tad

Thank You all very much for your submissions. We will be choosing a candidate today. We love this service, you all did awesome.

Thanks
Tad

Target Market(s)

Commerical businesses shipping freight and courier packages.

Industry/Entity Type

It Company

Requirements
Must have
• Flyer must be free of copyright.

```html
<!DOCTYPE html>
<html lang="en">
<head>
<meta charset="utf-8">
<title>MIDWAY PARCELRUN – Flyer</title>
<link rel="stylesheet" href="https://fonts.googleapis.com/css2?family=Libre+Baskerville:ital,wght@0,700;1,400;1,700&family=Nunito:ital,wght@0,900;1,900&family=Roboto+Condensed:wght@700&display=swap">
<style>
  :root {
    --frame: #2b2422;
    --blue: #0f77bd;
    --blue-dark: #0b5f9e;
    --blue-light: #29a3dc;
    --ink: #151515;
    --paper: #ffffff;
    --silver-light: #eeeeee;
    --silver-dark: #a9a9a9;
    --red: #e11b22;
    --red-dark: #a50f14;
  }
  * { margin: 0; padding: 0; box-sizing: border-box; }
  html, body { width: 849px; height: 1200px; overflow: hidden; background: var(--frame); }
  .flyer {
    position: relative; width: 849px; height: 1200px;
    background: var(--frame); padding: 20px;
  }
  .sheet {
    position: relative; width: 809px; height: 1160px; overflow: hidden;
    background: linear-gradient(180deg, #ffffff 0%, #f3f4f6 45%, #e6e8eb 70%);
  }
  .focus-band {
    position: absolute; left: 0; top: 42px; width: 100%; height: 98px;
    background: linear-gradient(180deg, var(--blue-light) 0%, var(--blue) 35%, var(--blue-dark) 100%);
  }
  .focus-band .speed-lines { position: absolute; left: 30px; top: 38px; }
  .focus-band .focus-line {
    position: absolute; left: 96px; top: 30px;
    font-family: "Libre Baskerville", serif; font-style: italic; font-weight: 700;
    font-size: 24px; color: var(--paper);
  }
  .fleet-art {
    position: absolute; left: 124px; top: 175px; width: 574px; height: 118px;
    background: linear-gradient(90deg, var(--blue) 0%, var(--blue-light) 100%);
    border-radius: 14px; opacity: .85;
  }
  .brand {
    position: absolute; left: 0; top: 335px; width: 100%; text-align: center;
  }
  .brand-name {
    font-family: "Nunito", sans-serif; font-weight: 900; font-size: 62px;
    letter-spacing: 1px; color: var(--blue); line-height: 1;
  }
  .brand-mark {
    display: inline-block; width: 22px; height: 22px; background: var(--blue);
    margin-right: 14px; vertical-align: 10px;
  }
  .tagline {
    position: absolute; left: 246px; top: 100px;
    font-family: "Libre Baskerville", serif; font-weight: 700; font-size: 21px; color: var(--ink);
  }
  .perk {
    position: absolute; font-family: "Libre Baskerville", serif; font-style: italic;
    font-weight: 700; color: var(--ink); white-space: nowrap;
  }
  .perk::after {
    content: ""; display: inline-block; width: 9px; height: 9px;
    background: var(--blue); margin-left: 6px; vertical-align: 2px;
  }
  .perk-xl { font-size: 17px; }
  .perk-l { font-size: 14px; }
  .perk-m { font-size: 12px; }
  .perk-s { font-size: 10px; }
  .call-badge { position: absolute; left: 20px; top: 650px; z-index: 5; }
  .call-lead {
    position: absolute; left: 214px; top: 684px;
    font-family: "Libre Baskerville", serif; font-weight: 700; font-size: 14px; color: var(--ink);
  }
  .toll-free {
    position: absolute; left: 204px; top: 702px;
    font-family: "Nunito", sans-serif; font-style: italic; font-weight: 900; font-size: 34px;
    color: var(--blue); letter-spacing: 1px;
    text-shadow: 0 0 2px #fff, 2px 2px 0 #0a4d80;
  }
  .silver-band {
    position: absolute; left: 0; width: 100%;
    background: linear-gradient(180deg, var(--silver-light) 0%, var(--silver-dark) 100%);
  }
  .silver-band.top { top: 770px; height: 47px; }
  .silver-band.bottom { top: 1130px; height: 30px; }
  .promo {
    position: absolute; left: 0; top: 817px; width: 100%; height: 313px;
    background: linear-gradient(180deg, var(--blue-dark) 0%, var(--blue) 60%, #1583c8 100%);
    color: var(--paper);
  }
  .promo-title {
    position: absolute; left: 0; top: 10px; width: 100%; text-align: center;
    font-family: "Nunito", sans-serif; font-weight: 900; font-size: 40px;
    text-shadow: 2px 2px 0 #0a3f6b;
  }
  .promo-route {
    position: absolute; left: 79px; top: 84px;
    font-family: "Roboto Condensed", sans-serif; font-weight: 700; font-size: 16px; line-height: 20px;
  }
  .promo-route .price { font-size: 22px; line-height: 30px; }
  .promo-terms {
    position: absolute; left: 76px; top: 162px;
    font-family: "Nunito", sans-serif; font-weight: 900; font-size: 31px; line-height: 35px;
    text-shadow: 2px 2px 0 #0a3f6b;
  }
  .surcharge-burst { position: absolute; left: 516px; top: 850px; z-index: 4; }
</style>
</head>
<body>
<div class="flyer">
  <div class="sheet">
    <header class="focus-band">
      <svg class="speed-lines" width="64" height="18" viewBox="0 0 64 18" aria-hidden="true">
        <rect x="0" y="0" width="64" height="3" fill="#fff"/>
        <rect x="8" y="7" width="56" height="3" fill="#fff"/>
        <rect x="16" y="14" width="48" height="3" fill="#fff"/>
      </svg>
      <p class="focus-line">Our focus is on the commercial shipping customer</p>
    </header>

    <div class="fleet-art" role="img" aria-label="Illustration of three blue delivery vans in decreasing size"></div>

    <div class="brand">
      <div class="brand-name"><span class="brand-mark"></span>MIDWAY PARCELRUN</div>
      <p class="tagline">every package is a priority</p>
    </div>

    <p class="perk perk-xl" style="left:58px; top:488px;">Overnight courier service</p>
    <p class="perk perk-m" style="left:400px; top:480px;">Friendly and reliable shipping experience</p>
    <p class="perk perk-m" style="left:292px; top:521px;">Guaranteed shipment will always arrive when stated</p>
    <p class="perk perk-l" style="left:141px; top:550px;">No package misplaced</p>
    <p class="perk perk-xl" style="left:481px; top:547px;">No extra fees</p>
    <p class="perk perk-m" style="left:57px; top:581px;">Traceable freight</p>
    <p class="perk perk-l" style="left:356px; top:582px;">Web based dispatch</p>
    <p class="perk perk-s" style="left:590px; top:602px;">On site services</p>

    <p class="call-lead">Call us now, because every package is a priority</p>
    <p class="toll-free">Toll Free 1.800.555.0142</p>

    <div class="silver-band top"></div>

    <section class="promo">
      <h2 class="promo-title">10 dollar triangle</h2>
      <p class="promo-route">Ship anywhere between Calgary<br>Lethbridge and Medicine Hat or anywhere point between<br><span class="price">for just 10 Bucks</span></p>
      <p class="promo-terms">Max weight 150lbs<br>Guarranteed Overnight<br>G.S.T. extra</p>
    </section>

    <div class="silver-band bottom"></div>

    <svg class="call-badge" width="170" height="170" viewBox="0 0 180 180" role="img" aria-label="Call us">
      <defs>
        <radialGradient id="callFill" cx="40%" cy="35%" r="70%">
          <stop offset="0%" stop-color="#ff4a4f"/>
          <stop offset="100%" stop-color="#b50d13"/>
        </radialGradient>
      </defs>
      <circle cx="90" cy="90" r="88" fill="#d8d8d8"/>
      <circle cx="90" cy="90" r="80" fill="#ffffff"/>
      <circle cx="90" cy="90" r="72" fill="url(#callFill)"/>
      <text x="30" y="86" font-family="Nunito, sans-serif" font-weight="900" font-style="italic" font-size="38" fill="#fff">Call</text>
      <text x="34" y="122" font-family="Nunito, sans-serif" font-weight="900" font-style="italic" font-size="36" fill="#fff">us</text>
      <path d="M112 96 c-6 6 -4 18 6 30 c10 12 22 16 28 10 l4-5 c2-2 1-5-1-6 l-9-6 c-2-1-4-1-5 1 l-3 3 c-5-2-11-9-13-14 l3-3 c2-1 2-4 1-5 l-6-9 c-1-2-4-3-6-1 z" fill="#fff"/>
    </svg>

    <svg class="surcharge-burst" width="260" height="260" viewBox="-130 -130 260 260" role="img" aria-label="No extra surcharges">
      <polygon fill="#e11b22" points="120,0 88.9,23.8 103.9,60 65.1,65.1 60,103.9 23.8,88.9 0,120 -23.8,88.9 -60,103.9 -65.1,65.1 -103.9,60 -88.9,23.8 -120,0 -88.9,-23.8 -103.9,-60 -65.1,-65.1 -60,-103.9 -23.8,-88.9 0,-120 23.8,-88.9 60,-103.9 65.1,-65.1 103.9,-60 88.9,-23.8"/>
      <polygon fill="#ffffff" transform="scale(.9)" points="120,0 88.9,23.8 103.9,60 65.1,65.1 60,103.9 23.8,88.9 0,120 -23.8,88.9 -60,103.9 -65.1,65.1 -103.9,60 -88.9,23.8 -120,0 -88.9,-23.8 -103.9,-60 -65.1,-65.1 -60,-103.9 -23.8,-88.9 0,-120 23.8,-88.9 60,-103.9 65.1,-65.1 103.9,-60 88.9,-23.8"/>
      <polygon fill="#e11b22" transform="scale(.82)" points="120,0 88.9,23.8 103.9,60 65.1,65.1 60,103.9 23.8,88.9 0,120 -23.8,88.9 -60,103.9 -65.1,65.1 -103.9,60 -88.9,23.8 -120,0 -88.9,-23.8 -103.9,-60 -65.1,-65.1 -60,-103.9 -23.8,-88.9 0,-120 23.8,-88.9 60,-103.9 65.1,-65.1 103.9,-60 88.9,-23.8"/>
      <g transform="rotate(-8)" font-family="Nunito, sans-serif" font-weight="900" font-style="italic" fill="#fff" stroke="#0b5f9e" stroke-width="1.5" text-anchor="middle">
        <text x="0" y="-18" font-size="40">NO</text>
        <text x="0" y="18" font-size="40">EXTRA</text>
        <text x="0" y="42" font-size="20">SURCHARGES</text>
      </g>
    </svg>
  </div>
</div>
</body>
</html>
```